It is a leisure sector investment company.The company plans to invest in a luxurious 5 star resort

We need a stationery design to our company 'Copper Lantern Limited' using the winning logo design. We need the letter heads, envelopes & the business cards. Should be simple, plain and professional
We have upload the source file & vector files which gives our logo design. We prefer the bottom logo.

Have updated under 'must have priorities', the company name, address, tel no. fax no. & the company reg no. which should come on the letter head. the long envelope should have the company name, tel & fax no. 
Business card should have the company name, name on the card, designation, tel no. fax no.  

- Letter head details:
Copper Lantern Limited
14 Floor, South Wing, Halvard Merchant Plaza,
Merrow Court, Colombo 01, Sri Lanka
Tel: +94 11 5047293 Fax: +94 11 5047298
Company Reg No.QX 6142
Long Envelope should have only the company name, adress, Tel & Fax
Business Cards should have the company name, Tel & Fax:
Business Card 1 - Lasantha Gunaratne - Chairman
Business Card 2 - Nimal.T.Wijesooriya - COO

```html
<!DOCTYPE html>
<html lang="en">
<head>
<meta charset="utf-8">
<title>Copper Lantern Limited – Business Card</title>
<link rel="stylesheet" href="https://fonts.googleapis.com/css2?family=Cinzel:wght@400&family=Tinos&display=swap">
<style>
  :root {
    --page: #ffffff;
    --card: #a8a56c;
    --card-deep: #97935e;
    --ink: #3f352e;
    --label: #000000;
  }
  * { margin: 0; padding: 0; box-sizing: border-box; }
  html, body { width: 1200px; height: 446px; overflow: hidden; background: var(--page); }
  .sheet { position: relative; width: 1200px; height: 446px; }
  .side-label {
    position: absolute; top: 28px;
    font: 21px "Tinos", "Times New Roman", serif; color: var(--label);
  }
  .side-label--front { left: 84px; }
  .side-label--back { left: 646px; }
  .card {
    position: absolute; width: 504px; height: 305px;
    background: var(--card); overflow: hidden;
  }
  .card--front { left: 70px; top: 70px; }
  .card--back { left: 629px; top: 71px; }
  .damask-band {
    position: absolute; left: 0; width: 100%; height: 80px;
  }
  .damask-band--top { top: 0; background: linear-gradient(180deg, var(--card-deep), var(--card)); }
  .damask-band--bottom { bottom: 0; background: linear-gradient(0deg, var(--card-deep), var(--card)); }
  .wordmark {
    position: absolute; left: 0; right: 0; top: 150px;
    text-align: center; color: var(--ink);
    font-family: "Cinzel", "Trajan Pro", serif; font-weight: 400; line-height: 1;
  }
  .wordmark__name { display: block; font-size: 42px; letter-spacing: 0.5px; }
  .wordmark__suffix { display: block; font-size: 28px; letter-spacing: 9px; margin-top: 8px; }
  .contact {
    position: absolute; left: 0; right: 0; top: 128px;
    text-align: center; color: var(--ink);
    font-family: "Tinos", "Times New Roman", serif;
  }
  .contact__name { font-size: 17px; }
  .contact__address { font-size: 10.5px; margin-top: 14px; }
  .contact__phones { font-size: 10.5px; margin-top: 17px; word-spacing: 1px; }
</style>
</head>
<body>
<main class="sheet">
  <span class="side-label side-label--front">FRONT</span>
  <span class="side-label side-label--back">BACK</span>

  <section class="card card--front">
    <div class="damask-band damask-band--top" role="img" aria-label="Faint olive damask scroll pattern across the top edge"></div>
    <div class="damask-band damask-band--bottom" role="img" aria-label="Faint olive damask scroll pattern across the bottom edge"></div>
    <h1 class="wordmark">
      <span class="wordmark__name">COPPER LANTERN</span>
      <span class="wordmark__suffix">LIMITED</span>
    </h1>
  </section>

  <section class="card card--back">
    <div class="contact">
      <p class="contact__name">Nimal .T. Wijesooriya - Coo</p>
      <p class="contact__address">14, floor, South Wing, Halvard Merchant Plaza, Merrow Court, Colombo 01, Sri Lanka</p>
      <p class="contact__phones">Tel No.&nbsp; +94 11 5047293&nbsp; Fax No.&nbsp; +94 11 5047298</p>
    </div>
  </section>
</main>
</body>
</html>
```